Luxury Skincare Product Box Packaging Design

Vorastelle is a range of skincare products that help protect, nourish, and strengthen even the most sensitive skin, ensuring it is healthy, glowing, calm, and soft. Skincare practices support skin to enhance its appearance and relieve skin conditions. Your skin reflects your health. It is your body canvas and is an asset. The products contain naturally derived ingredients, aromatherapy oils, sustainable and ethical ingredients, organic ingredients where possible, natural preservatives and Australian oils, fruits, and extracts.

Vorastelle
Tagline is "Where Calm Finds Bloom"

Our products do not contain sulphates, parabens, phthalates, petrochemicals, synthetic colours, nor synthetic fragrances.

Everything about the Vorastelle Skincare name is creative and communicates luxury. Vorastelle from your first glance of the name, you will know that this is a company with excellent products.

By keeping it simple, unique, and elegant is often associated with high quality and is a way to establish trust. Vorastelle is a product that is “pure” and natural, so Vorastelle packaging would look simple, elegant, and clean.

I have uploaded the actual logo design and individual labels for the current skincare range I currently with the ingredients included so you can get an understanding of what I like. I have also added samples of package designs I quite like to assist with your designs.

Each Product box packaging sizes are as follows:

Product One - Exfoliating Herbs: 110mm (H) x 33mm Diameter
Product Two - Probiotic Lotion: 138mm (H) x 33mm Diameter
Product Three - Vitamin A Serum: 120mm (H) x 30mm Diameter
Updates

The Measurements are as follows: Product One: 110mm (H) x 33mm Diameter Product Two: 138mm (H) x 33mm Diameter Product Three: 120mm (H) x 30mm Diameter

Target Market(s)

Women

Requirements
Must have
• Logo, Product Name and ingredients and if you can barcode on the packaging that is the box design I am after
Nice to have
• samples of designs I like but open to suggestions

```html
<!DOCTYPE html>
<html lang="en">
<head>
<meta charset="utf-8">
<title>Vorastelle – Gentle Exfoliating Herbs Packaging</title>
<link rel="stylesheet" href="https://fonts.googleapis.com/css2?family=Marcellus&family=Montserrat:wght@400;500&display=swap">
<style>
  :root {
    --backdrop: #d2a197;
    --panel-blush: #dcc6ba;
    --panel-cloud: #d8d8d8;
    --panel-mist: #c9c9c9;
    --label-white: #ececec;
    --ink-grey: #645e5c;
    --ink-dark: #2a2a2a;
    --blob-charcoal: #5f5f5f;
    --blob-mauve: #a77a72;
    --bronze: #9c6b58;
    --foliage-light: #c7a08e;
    --foliage-deep: #8f6452;
    --text-light: #f1ece9;
  }
  html, body {
    margin: 0;
    width: 1200px;
    height: 800px;
    overflow: hidden;
    background: var(--backdrop);
  }
  .stage {
    position: relative;
    width: 1200px;
    height: 800px;
  }
  .box-front {
    position: absolute;
    left: 418px;
    top: 172px;
    width: 183px;
    height: 481px;
  }
  .bottle-label {
    position: absolute;
    left: 642px;
    top: 430px;
    width: 146px;
    height: 168px;
  }
  .wordmark {
    font-family: "Marcellus", serif;
    fill: var(--bronze);
  }
  .tagline {
    font-family: "Montserrat", sans-serif;
    font-weight: 500;
    fill: var(--ink-dark);
  }
  .product-name {
    font-family: "Marcellus", serif;
    fill: var(--ink-grey);
    letter-spacing: 2px;
  }
  .label-product-name {
    font-family: "Marcellus", serif;
    fill: var(--text-light);
    letter-spacing: 0.8px;
  }
  .label-small {
    font-family: "Montserrat", sans-serif;
    fill: var(--text-light);
  }
  .label-volume {
    font-family: "Montserrat", sans-serif;
    fill: var(--ink-grey);
  }
</style>
</head>
<body>
<main class="stage">

  <svg class="box-front" viewBox="0 0 183 481" xmlns="http://www.w3.org/2000/svg">
    <defs>
      <linearGradient id="foliage-tone" x1="0" y1="0" x2="1" y2="1">
        <stop offset="0" stop-color="var(--foliage-light)"/>
        <stop offset="1" stop-color="var(--foliage-deep)"/>
      </linearGradient>
    </defs>
    <rect class="box-base" width="183" height="481" fill="var(--panel-blush)"/>
    <path class="box-cloud-top" fill="var(--panel-cloud)"
      d="M0 25 C30 8 80 -2 120 2 C150 6 170 40 183 68 L183 265 C160 285 120 285 90 280 C60 272 45 250 40 230 C30 214 15 212 0 214 Z"/>
    <path class="box-cloud-bottom" fill="var(--panel-mist)"
      d="M0 430 C30 412 80 410 120 418 C150 425 170 440 183 450 L183 481 L0 481 Z"/>
    <path class="foliage-art" role="img" aria-label="Bronze leaf sprig illustration"
      fill="url(#foliage-tone)" opacity="0.85"
      d="M50 395 C80 380 110 360 130 330 C150 305 170 300 183 300 L183 481 L150 481 C120 465 90 445 70 425 C60 415 52 405 50 395 Z"/>
    <text class="wordmark" font-size="36" transform="translate(82 300) rotate(-90)">Vorastelle</text>
    <text class="tagline" font-size="8" letter-spacing="2.2" transform="translate(118 200) rotate(-90)">Where Calm Finds Bloom</text>
    <text class="product-name" font-size="14">
      <tspan x="26" y="337">GENTLE</tspan>
      <tspan x="26" y="353">EXFOLIATING</tspan>
      <tspan x="26" y="369">HERBS</tspan>
    </text>
  </svg>

  <svg class="bottle-label" viewBox="0 0 146 168" xmlns="http://www.w3.org/2000/svg">
    <rect class="label-base" width="146" height="168" fill="var(--panel-blush)"/>
    <path class="label-cloud-top" fill="var(--label-white)"
      d="M0 0 L146 0 L146 95 C120 100 105 92 95 80 C85 68 70 62 50 62 C30 62 10 58 0 50 Z"/>
    <path class="label-cloud-bottom" fill="var(--label-white)"
      d="M90 168 C92 150 110 138 130 138 C138 138 143 140 146 142 L146 168 Z"/>
    <ellipse class="label-mauve-spot" cx="18" cy="62" rx="16" ry="10" fill="var(--blob-mauve)"/>
    <path class="label-charcoal-blob" fill="var(--blob-charcoal)"
      d="M10 88 C20 78 55 76 70 90 C78 98 74 110 84 118 C94 126 92 140 78 144 C60 149 40 156 20 154 C6 152 4 140 10 130 C16 118 2 102 10 88 Z"/>
    <path class="label-foliage-art" role="img" aria-label="Bronze leaf sprig illustration"
      fill="url(#foliage-tone)" opacity="0.8"
      d="M70 140 C90 128 105 110 115 95 C125 80 138 78 146 80 L146 130 C130 140 115 150 100 160 C90 165 78 160 70 140 Z"/>
    <text class="wordmark" font-size="17" text-anchor="middle" x="80" y="30">Vorastelle</text>
    <text class="tagline" font-size="4.2" letter-spacing="0.6" text-anchor="middle" x="88" y="38">Where Calm Finds Bloom</text>
    <text class="label-product-name" font-size="7">
      <tspan x="18" y="97">GENTLE</tspan>
      <tspan x="18" y="104">EXFOLIATING</tspan>
      <tspan x="18" y="111">HERBS</tspan>
    </text>
    <text class="label-small" font-size="4.5" letter-spacing="0.4" x="18" y="138">All Skin Types</text>
    <text class="label-volume" font-size="4.5" letter-spacing="0.6" x="68" y="160">50ML</text>
  </svg>

</main>
</body>
</html>
```